Dential Clinic Business Card

We need a simple elegant business card. 2 sided. First side with our details, and 2nd side with appointment time rows.

Dark background preferred. Will consider monotone design, or colored. Surprise us.

Details:
SIDE1

Maplewood Square Dental

Dr Peter Hollis
BDSc(Adel) FRZPTA

Shop 42, Maplewood Square
7-19 Birch Parade, Elmvale VIC 3999
Phone: 03 9555 0148
email: info@maplewoodsquaredental.com.au
site: www.maplewoodsquaredental.com.au
_____________________________________
SIDE 2
Appointed Time ________________________
Notes _______________________

Target Market(s)

Dental Patients

Industry/Entity Type

Healthcare

Contact Information for Business Card

SIDE1

Maplewood Square Dental

Dr Peter Hollis
Shop 42, Maplewood Square
Phone: 03 9555 0148
SIDE 2

Font styles to use
Other font styles liked:
• Comfortaa

Requirements
Must have
• Dr Peter Hollis
BDSc(Adel) FRZPTA

Address
Phone
Email
Website
Nice to have
• Simple elegant design with our logo.
Colored logo.
Light text on dark background - Side 1
Light background so can be written on with dark pen - SIde 2
Should not have
• Too many colors

```html
<!DOCTYPE html>
<html lang="en">
<head>
<meta charset="utf-8">
<title>Maplewood Square Dental – Business Card</title>
<link href="https://fonts.googleapis.com/css2?family=Lato:wght@400;700&display=swap" rel="stylesheet">
<style>
  :root {
    --stage: #d6d6d6;
    --card-dark: #0f1012;
    --card-light: #ffffff;
    --brand-blue: #1b95d3;
    --brand-green: #7cc242;
    --text-grey: #a7a9ac;
  }
  * { box-sizing: border-box; margin: 0; padding: 0; }
  html, body {
    width: 1200px; height: 1143px; overflow: hidden;
    background: var(--stage);
    font-family: "Lato", sans-serif;
  }
  .card {
    position: absolute; left: 299px; width: 602px; height: 344px;
    box-shadow: 0 18px 30px rgba(0,0,0,0.28);
  }
  .card-front { top: 180px; background: var(--card-dark); }
  .card-back { top: 621px; background: var(--card-light); }

  .brand {
    position: absolute; display: flex; align-items: center; gap: 10px;
    font-size: 25px; font-weight: 400; color: var(--brand-blue);
    white-space: nowrap;
  }
  .brand-dot {
    width: 30px; height: 30px; border-radius: 50%;
    border: 3px solid var(--brand-green);
  }
  .card-front .brand { right: 37px; top: 71px; }
  .card-back .brand { left: 50%; transform: translateX(-50%); top: 62px; }

  .holder-name {
    position: absolute; left: 29px; top: 200px;
    font-size: 20px; font-weight: 700; color: var(--brand-blue);
  }
  .holder-name .surname { color: var(--brand-green); }
  .holder-role {
    position: absolute; left: 29px; top: 226px;
    font-size: 13.5px; color: var(--text-grey);
  }
  .divider {
    position: absolute; left: 29px; width: 544px; top: 252px;
    height: 1px; background: var(--brand-blue);
  }
  .contact-list { position: absolute; left: 29px; top: 263px; list-style: none; }
  .contact-list li {
    display: flex; align-items: center; height: 19px;
    font-size: 13px; color: var(--text-grey);
  }
  .contact-list svg { width: 13px; height: 13px; margin-right: 11px; fill: var(--brand-green); }
  .address {
    position: absolute; right: 29px; top: 285px; text-align: right;
    font-size: 13px; line-height: 16.5px; color: var(--text-grey);
    font-style: normal;
  }

  .appointment-title {
    position: absolute; left: 0; right: 0; top: 150px; text-align: center;
    font-size: 30px; font-weight: 700; color: var(--brand-blue);
  }
  .field {
    position: absolute; left: 32px; right: 32px; display: flex; align-items: flex-end;
    font-size: 19px; color: var(--brand-blue);
  }
  .field .rule { flex: 1; height: 1px; background: var(--brand-green); margin: 0 0 4px 6px; }
  .field-time { top: 206px; }
  .field-notes { top: 247px; }
  .days {
    position: absolute; left: 0; top: 286px; width: 100%; height: 22px;
    list-style: none;
  }
  .days li {
    position: absolute; display: flex; align-items: center; gap: 9px;
    font-size: 19px; letter-spacing: 2px; color: var(--brand-blue);
  }
  .days .box {
    width: 16px; height: 16px; border-radius: 50%;
    border: 2.5px solid var(--brand-green);
  }
</style>
</head>
<body>

<section class="card card-front" aria-label="Business card front">
  <div class="brand"><span class="brand-dot"></span>Maplewood Square Dental</div>

  <h1 class="holder-name">Dr Peter <span class="surname">Hollis</span></h1>
  <p class="holder-role">Principal Dentist</p>
  <div class="divider"></div>

  <ul class="contact-list">
    <li>
      <svg viewBox="0 0 16 16" aria-hidden="true"><path d="M1 5c0-2 3-3 7-3s7 1 7 3v1.5h-3.5V5h-7v1.5H1z"/><path d="M3 8l2-2h6l2 2v6H3z"/><circle cx="8" cy="10.5" r="1.8" fill="#0f1012"/></svg>
      03 9555 0148
    </li>
    <li>
      <svg viewBox="0 0 16 16" aria-hidden="true"><path d="M1 3h14v10H1z"/><path d="M1.5 3.5L8 9l6.5-5.5" stroke="#0f1012" stroke-width="1.2" fill="none"/><path d="M1.5 12.5L6 8M14.5 12.5L10 8" stroke="#0f1012" stroke-width="1" fill="none"/></svg>
      info@maplewoodsquaredental.com.au
    </li>
    <li>
      <svg viewBox="0 0 16 16" aria-hidden="true"><circle cx="8" cy="8" r="7"/><g stroke="#0f1012" stroke-width="0.9" fill="none"><ellipse cx="8" cy="8" rx="3" ry="6.2"/><path d="M1.5 8h13M2.5 4.8h11M2.5 11.2h11M8 1.5v13"/></g></svg>
      www.maplewoodsquaredental.com.au
    </li>
  </ul>

  <address class="address">
    Shop 42, Maplewood Square<br>
    7-19 Birch Parade, Elmvale VIC 3999
  </address>
</section>

<section class="card card-back" aria-label="Appointment card back">
  <div class="brand"><span class="brand-dot"></span>Maplewood Square Dental</div>

  <h2 class="appointment-title">APPOINTMENT</h2>

  <div class="field field-time">Time:<span class="rule"></span></div>
  <div class="field field-notes">Notes:<span class="rule"></span></div>

  <ul class="days">
    <li style="left:50px"><span class="box"></span>Mon</li>
    <li style="left:141px"><span class="box"></span>Tue</li>
    <li style="left:226px"><span class="box"></span>Wed</li>
    <li style="left:315px"><span class="box"></span>Thur</li>
    <li style="left:410px"><span class="box"></span>Fri</li>
    <li style="left:497px"><span class="box"></span>Sat</li>
  </ul>
</section>

</body>
</html>
```